Business Card Design

residential construction discipline, renovation additions, new homes, also sheds, retaining walls and general building maintenance. In house design and construct, estimate or bill of quantities, complete project administration, contract administration. design and construction Negotiations and consultation.complete council submissions for consent. Sustainable design and construction. The design will need to be smart colorful fine line(s), impressive. Font will need to be palatino linotype, the "a" in volrept will need to be a eco green color and the rest of the lettering black or sky blue. present initial proof design for review
Industry/Entity Type
Construction
Contact Information for Business Card
Kivortel Pty Ltd
ABN: 52 839 274 610
ACN: 839 274 610
Lic/Reg Number: 604172
Director: Trevor Dallow BConstructMgmt&Eco, AssocDegBuiltEnv
Building Works Supervisor
Lic/Reg Number: BLD681429
Email: kivortel@mailbrook.net
Mobile: 0431 958 204
Fax: (08) 8261 3095
Look and feel

```html
<!DOCTYPE html>
<html lang="en">
<head>
<meta charset="utf-8">
<title>Kivortel Pty Ltd – Business Card</title>
<link rel="stylesheet" href="https://fonts.googleapis.com/css2?family=Open+Sans:wght@400;600&family=Michroma&display=swap">
<style>
  :root {
    --backdrop: #6a6a6a;
    --card-white: #ffffff;
    --card-shade: #e4e4e4;
    --brand-blue: #1f6fc4;
    --band-deep: #2f52bd;
    --band-sky: #1ea0e6;
    --eco-green: #1f9a3e;
    --ink: #333333;
    --ink-soft: #555555;
  }
  * { box-sizing: border-box; margin: 0; padding: 0; }
  html, body { width: 1200px; height: 750px; overflow: hidden; }
  body {
    background: var(--backdrop);
    font-family: "Open Sans", sans-serif;
    position: relative;
  }
  .card {
    position: absolute;
    width: 540px;
    height: 310px;
    border-radius: 22px;
    overflow: hidden;
    background: radial-gradient(ellipse at 45% 40%, var(--card-white) 35%, var(--card-shade) 100%);
    box-shadow: 0 10px 28px rgba(0,0,0,.35);
  }
  .card--back { left: 40px; top: 130px; }
  .card--front { left: 620px; top: 310px; }

  .brand {
    display: flex;
    align-items: center;
    gap: 14px;
  }
  .brand__disc {
    width: 58px; height: 58px;
    border-radius: 50%;
    background: var(--brand-blue);
    flex: none;
  }
  .brand__name {
    font-family: "Open Sans", sans-serif;
    font-weight: 600;
    font-size: 26px;
    color: var(--brand-blue);
    white-space: nowrap;
  }

  .card--back .brand { position: absolute; left: 120px; top: 70px; }
  .services {
    position: absolute;
    left: 50px; right: 50px; top: 160px;
    text-align: center;
    font-size: 14px;
    line-height: 1.45;
    color: var(--ink);
  }

  .band { position: absolute; left: 0; top: 0; width: 540px; height: 310px; }
  .holder__name {
    font-family: "Michroma", sans-serif;
    font-size: 13px;
    letter-spacing: 2px;
    fill: #fff;
  }
  .holder__quals {
    font-family: "Open Sans", sans-serif;
    font-size: 9px;
    fill: #fff;
  }
  .card--front .brand { position: absolute; left: 150px; top: 150px; }
  .contacts {
    position: absolute;
    left: 32px; bottom: 22px;
    font-size: 9.5px;
    color: var(--ink-soft);
    line-height: 1.8;
  }
  .contacts__row { display: flex; gap: 12px; align-items: center; white-space: nowrap; }
  .contacts__item { display: inline-flex; align-items: center; gap: 4px; font-family: "Michroma", sans-serif; font-size: 8.5px; }
  .contacts__icon { width: 11px; height: 11px; }
</style>
</head>
<body>

<section class="card card--back" aria-label="Card back">
  <div class="brand">
    <span class="brand__disc"></span>
    <span class="brand__name">Kivortel Pty Ltd</span>
  </div>
  <p class="services">New Homes from single story to multilevel, additions and renovations, estimates and BQ, construction &amp; Project management, in house design, Council consultation, subdivisions, building maintenance.</p>
</section>

<section class="card card--front" aria-label="Card front">
  <svg class="band" viewBox="0 0 540 310">
    <defs>
      <linearGradient id="bandFill" x1="0" y1="0" x2="1" y2="0">
        <stop offset="0" stop-color="#2f52bd"/>
        <stop offset="0.45" stop-color="#1ea0e6"/>
        <stop offset="1" stop-color="#2f52bd"/>
      </linearGradient>
      <path id="nameLine" d="M20 112 Q300 26 540 6"/>
      <path id="qualsLine" d="M10 140 Q300 52 536 26"/>
    </defs>
    <path d="M0 0 H540 V32 Q300 55 0 150 Z" fill="url(#bandFill)"/>
    <path d="M0 150 Q300 55 540 32 V44 Q300 68 0 164 Z" fill="var(--eco-green)"/>
    <text class="holder__name" text-anchor="middle">
      <textPath href="#nameLine" startOffset="46%">TREVOR DALLOW | DIRECTOR</textPath>
    </text>
    <text class="holder__quals" text-anchor="middle">
      <textPath href="#qualsLine" startOffset="50%">BConstructMgmt&amp;Eco, AssocDegBuiltEnv Building Works Supervisor Lic/Reg Number: BLD681429</textPath>
    </text>
  </svg>

  <div class="brand">
    <span class="brand__disc"></span>
    <span class="brand__name">Kivortel Pty Ltd</span>
  </div>

  <div class="contacts">
    <p class="contacts__row">ABN: 52 839 274 610 | ACN: 839 274 610 | Lic/Reg Number: 604172</p>
    <p class="contacts__row">
      <span class="contacts__item">
        <svg class="contacts__icon" viewBox="0 0 12 12" aria-hidden="true"><circle cx="6" cy="6" r="6" fill="var(--eco-green)"/><path d="M4 3 L5 3 L5.6 4.6 L4.9 5.2 Q5.6 6.6 6.8 7.1 L7.4 6.4 L9 7 L9 8 Q7.5 9.2 5 7.2 Q3 5 4 3 Z" fill="#fff"/></svg>
        0431 958 204
      </span>
      <span class="contacts__item">
        <svg class="contacts__icon" viewBox="0 0 12 12" aria-hidden="true"><circle cx="6" cy="6" r="6" fill="var(--eco-green)"/><rect x="3" y="4" width="6" height="4.5" rx="0.6" fill="#fff"/><rect x="4" y="2.5" width="4" height="2" fill="#fff"/></svg>
        (08) 8261 3095
      </span>
      <span class="contacts__item">
        <svg class="contacts__icon" viewBox="0 0 12 12" aria-hidden="true"><circle cx="6" cy="6" r="6" fill="var(--eco-green)"/><rect x="2.8" y="3.8" width="6.4" height="4.4" fill="#fff"/><path d="M2.8 3.8 L6 6.3 L9.2 3.8" fill="none" stroke="var(--eco-green)" stroke-width="0.7"/></svg>
        kivortel@mailbrook.net
      </span>
    </p>
  </div>
</section>

</body>
</html>
```